KRL Banner Logo with Rocky Mountain of CO as the background

I need a banner/logo for my KRL year. So have a banner design that is like an intentional path or inspiring.

• KRL Silver Ridge CO mountain as background and they may add similar images that I sent you
• Wording: Intentional Path
Learning year 2025-2026
• Add the KRL logo (the white and blue image – you will see these online)

UPDATE: Attached are example images on how we envision the banner. Please do not use the attached example sample images. Kindly look for similar looking images that are FREE TO USE Commercially.

CEO, top executives

0054AA
0677BA
7BADD7
CADEEF
E8F1F8

• • KRL Silver Ridge CO mountain as background and they may add similar images that I sent you • Wording: Intentional Path Learning year 2025-2026 • Add the KRL logo (the white and blue image – you will see these online)
• It has nice to have the inspirational images attached but you can have your own design. This is only for sample.

```html
<!DOCTYPE html>
<html lang="en">
<head>
<meta charset="utf-8">
<title>Intentional Path – Learning Year 2025-2026</title>
<link href="https://fonts.googleapis.com/css2?family=Playfair+Display:wght@900&family=Montserrat:wght@700&display=swap" rel="stylesheet">
<style>
  :root {
    --paper: #ffffff;
    --paper-shade: #e9e7e3;
    --ink-navy: #18284a;
    --sky-top: #5f7fa6;
    --sky-cloud: #d5dbe2;
    --rock-sunlit: #8d7466;
    --rock-shadow: #4c4852;
    --slope-dark: #2f2b2c;
    --valley: #211e1d;
  }
  * { margin: 0; padding: 0; box-sizing: border-box; }
  html, body {
    width: 1200px;
    height: 601px;
    overflow: hidden;
    background: var(--paper);
  }
  .banner {
    position: relative;
    width: 1200px;
    height: 601px;
    background: var(--paper);
    overflow: hidden;
  }
  .banner__photo {
    position: absolute;
    inset: 0;
  }
  .banner__title-block {
    position: absolute;
    left: 20px;
    width: 480px;
    top: 132px;
    text-align: center;
    color: var(--ink-navy);
  }
  .banner__title {
    font-family: "Playfair Display", Georgia, serif;
    font-weight: 900;
    font-size: 58px;
    line-height: 1.38;
    letter-spacing: 1px;
    text-transform: uppercase;
  }
  .banner__subtitle {
    margin-top: 40px;
    font-family: "Montserrat", Arial, sans-serif;
    font-weight: 700;
    font-size: 25px;
    letter-spacing: 1.2px;
    text-transform: uppercase;
  }
  .banner__brand {
    position: absolute;
    left: 178px;
    top: 498px;
    display: flex;
    align-items: center;
    gap: 12px;
    color: var(--ink-navy);
    font-family: "Montserrat", Arial, sans-serif;
    font-weight: 700;
    font-size: 36px;
    letter-spacing: 1px;
  }
  .banner__brand-mark {
    width: 34px;
    height: 34px;
    background: var(--ink-navy);
  }
</style>
</head>
<body>
  <main class="banner">
    <svg class="banner__photo" width="1200" height="601" viewBox="0 0 1200 601" role="img" aria-label="Photograph of jagged sunlit Rocky Mountain peaks under a cloudy blue sky, with dark snow-dusted slopes below">
      <defs>
        <linearGradient id="mountain-base" x1="0" y1="0" x2="0" y2="1">
          <stop offset="0" stop-color="var(--sky-top)"/>
          <stop offset="0.12" stop-color="var(--sky-cloud)"/>
          <stop offset="0.22" stop-color="#a9b0bb"/>
          <stop offset="0.34" stop-color="var(--rock-shadow)"/>
          <stop offset="0.55" stop-color="#3d3639"/>
          <stop offset="0.68" stop-color="var(--slope-dark)"/>
          <stop offset="1" stop-color="var(--valley)"/>
        </linearGradient>
        <radialGradient id="sunlit-rock" cx="0.4" cy="0.42" r="0.38">
          <stop offset="0" stop-color="var(--rock-sunlit)" stop-opacity="0.85"/>
          <stop offset="1" stop-color="var(--rock-sunlit)" stop-opacity="0"/>
        </radialGradient>
        <radialGradient id="cloud-glow" cx="0.35" cy="0.08" r="0.45">
          <stop offset="0" stop-color="#eef1f4" stop-opacity="0.9"/>
          <stop offset="1" stop-color="#eef1f4" stop-opacity="0"/>
        </radialGradient>
        <radialGradient id="snow-haze" cx="0.75" cy="0.72" r="0.35">
          <stop offset="0" stop-color="#8d9199" stop-opacity="0.45"/>
          <stop offset="1" stop-color="#8d9199" stop-opacity="0"/>
        </radialGradient>
      </defs>
      <rect x="420" width="780" height="601" fill="url(#mountain-base)"/>
      <rect x="420" width="780" height="601" fill="url(#cloud-glow)"/>
      <rect x="420" width="780" height="601" fill="url(#sunlit-rock)"/>
      <rect x="420" width="780" height="601" fill="url(#snow-haze)"/>

      <path class="banner__paper-fringe" fill="var(--paper-shade)"
        d="M0,0 L540,0 C536,10 544,18 538,28 C533,38 546,46 541,58 C537,68 532,74 539,86
           C545,98 533,106 536,118 C539,128 528,136 531,148 C534,160 522,168 526,180
           C530,192 518,198 520,212 C522,224 512,232 516,244 C520,256 506,262 509,276
           C512,290 500,298 504,312 C508,324 494,332 497,346 C500,358 488,366 491,380
           C494,394 481,402 483,416 C485,430 473,438 476,452 C479,466 466,474 468,488
           C470,502 458,510 461,524 C464,538 452,546 454,560 C456,574 446,582 450,601 L0,601 Z"/>
      <path class="banner__paper" fill="var(--paper)"
        d="M0,0 L528,0 C524,12 533,20 526,32 C521,42 533,50 528,62 C524,72 519,80 526,92
           C531,102 520,110 523,122 C526,132 515,140 518,152 C521,164 509,170 513,184
           C516,196 505,202 507,216 C509,228 498,236 502,248 C506,260 493,266 496,280
           C499,294 487,300 491,314 C494,326 481,334 484,348 C487,360 475,368 478,382
           C481,396 468,404 470,418 C472,432 460,440 463,454 C466,468 453,476 455,490
           C457,504 445,512 448,526 C451,540 439,548 441,562 C443,576 433,586 437,601 L0,601 Z"/>
    </svg>

    <section class="banner__title-block">
      <h1 class="banner__title">Intentional<br>Path</h1>
      <p class="banner__subtitle">Learning Year 2025-2026</p>
    </section>

    <div class="banner__brand">
      <span class="banner__brand-mark"></span>
      <span class="banner__brand-name">KRL</span>
    </div>
  </main>
</body>
</html>
```